Hand-Crafted Furniture Company

We are working with Brammvok to build a new website for them.

Some sites to use for content/competitors and inspiration:

https://quintalfurniture.example
https://ashbelhome.example
https://www.pelgravik.example
https://www.dunsmarewoodworks.example

Thank you for taking the time to consider designing a website for us. We are web developers based in Stockton, CA, USA. Most of our projects go through the same process. Understanding this process may help you win a project with us. We custom-code all of our websites in-house. We don’t have any requirements as to what tools you use for your design, but we prefer Figma files. For any design that we label as four stars, we send it to the client for review. The client picks the final design they want us to use. Once we complete this process, we will continue to show additional clients all the four-star sites and purchase them later. Your designs will have multiple chances to sell. For better chances of success, we ask that you follow these guidelines.

IMAGES:
If you use any images or icons in the design, we ask that you have a link to the asset so we can purchase the image/icon. Most of the designs we submit do not have the customer’s images on them unless they have some great images. Be creative; show us the feeling you are trying to portray with your image choices. Use any royalty-free site you choose. We subscribe to Adobe and mainly use their images, but we can purchase images outside of Adobe. PLEASE NOTE: we will not submit designs to clients with watermarks on the images.

FONTS:
We ask that you identify the fonts used in the design. This can be done in a message if you want. We typically use Google Fonts and Adobe Fonts.

CONTENT:
We're always open to different content and ideas. We often submit designs with stock images so the client can see our vision. We typically take pictures after the website launch to use their images with our vision. Lorem Ipsum is fine for paragraphs, but we ask that you write the headers in correct English. We want to be able to show the vision and identify the sections of the website.

INSPIRATION:
We typically add a couple of links in the brief of websites we like to help you get started in your design.

REVISIONS:
We do not often ask for revisions of the designs unless we see something in the design that may not appeal to the client. If there are slight changes that we want to make, we do that in the development process.

FEEDBACK:
We rarely give feedback on designs during the design process. We are working on many website projects and do not have the time to provide feedback. We usually respond if your request is well thought out and asks specific questions, but a note asking “feedback, please” usually goes unanswered.

```html
<!DOCTYPE html>
<html lang="en">
<head>
<meta charset="utf-8">
<title>Brammvok — Hand-Crafted Furniture</title>
<link href="https://fonts.googleapis.com/css2?family=Jost:wght@400;500&family=Tinos:wght@400;700&display=swap" rel="stylesheet">
<style>
:root{
  --brown:#7d6049;
  --tan:#c79a64;
  --ink:#1d1d1d;
  --muted:#555;
  --line:#9a9a9a;
  --white:#ffffff;
}
*{box-sizing:border-box;margin:0;padding:0}
html,body{width:1200px;height:4695px;overflow:hidden;background:var(--white)}
body{position:relative;font-family:'Jost',sans-serif;color:var(--ink)}
.abs{position:absolute}
.center-x{transform:translateX(-50%);white-space:nowrap}

/* header */
.site-header{position:absolute;left:0;top:0;width:1200px;height:126px}
.nav-link{position:absolute;top:72px;font-size:13px;letter-spacing:2px;transform:translateX(-50%);white-space:nowrap}
.brand{position:absolute;top:48px;left:600px;transform:translateX(-50%);font-size:34px;font-weight:500;color:var(--brown);letter-spacing:1px;line-height:1}
.cart{position:absolute;left:1086px;top:66px}

/* hero */
.hero{position:absolute;left:0;top:126px;width:1200px;height:700px;background:linear-gradient(180deg,#d8d8d8 0%,#b8b8b8 45%,#7e7e7e 80%,#5e5e5e 100%)}
.hero-title{position:absolute;left:600px;top:150px;font-size:52px;letter-spacing:9px;font-weight:400;color:#111}
.hero-sub{position:absolute;left:600px;top:604px;font-size:27px;letter-spacing:3px;color:#fff}
.slide-arrow{position:absolute;width:46px;height:48px;background:#fff;display:flex;align-items:center;justify-content:center}

/* sections */
.section-title{position:absolute;left:600px;font-size:26px;letter-spacing:4px;font-weight:400}
.tile{position:absolute}
.tile-label{position:absolute;font-size:15px;letter-spacing:2.5px;transform:translateX(-50%);white-space:nowrap}

.feature{position:absolute;left:0;top:1875px;width:1200px;height:752px;background:linear-gradient(160deg,#b9b9b6 0%,#9d9a95 45%,#b59a78 75%,#c6a985 100%)}
.shop-btn{position:absolute;left:84px;top:657px;width:244px;height:47px;background:#fff;font-size:16px;display:flex;align-items:center;justify-content:center}

.product-name{position:absolute;top:3084px;font-size:20px}
.price{position:absolute;font-size:16px;display:flex;align-items:center;gap:12px}
.swatch{width:18px;height:14px;display:inline-block}
.carousel-arrow{position:absolute;top:2904px;width:44px;height:44px;background:rgba(255,255,255,.6);display:flex;align-items:center;justify-content:center}

/* connect */
.connect-photo{position:absolute;left:0;top:3263px;width:598px;height:655px;background:linear-gradient(170deg,#f1f0ec 0%,#e3e1db 55%,#cfc7b8 100%)}
.brand-small{position:absolute;left:861px;top:3404px;transform:translateX(-50%);font-size:38px;font-weight:500;color:var(--brown);letter-spacing:1px}
.connect-title{position:absolute;left:677px;top:3520px;font-family:'Tinos',serif;font-size:29px}
.field-label{position:absolute;font-family:'Tinos',serif;font-size:14px;letter-spacing:.5px}
.field{position:absolute;border:1px solid var(--line);background:#fff}
.submit-btn{position:absolute;left:782px;top:3774px;width:157px;height:44px;background:var(--brown);color:#fff;font-family:'Tinos',serif;font-weight:700;font-size:15px;display:flex;align-items:center;justify-content:center}

/* testimonials */
.testimonial{position:absolute;top:4150px;width:320px;transform:translateX(-50%);text-align:center;font-size:11.5px;line-height:26px}
.testimonial-name{display:block;margin-top:22px;font-weight:500;font-size:12px}

/* footer */
.site-footer{position:absolute;left:0;top:4410px;width:1200px;height:285px;background:var(--brown);color:#fff;font-size:12px}
.foot-item{position:absolute}
.social-dot{position:absolute;top:88px;width:18px;height:18px;border:2px solid #fff;border-radius:50%}
.foot-email{position:absolute;left:768px;top:168px;width:190px;height:33px;border:1px solid #fff;padding:0 14px;display:flex;align-items:center}
.foot-signup{position:absolute;left:958px;top:168px;width:87px;height:33px;background:#fff;color:var(--brown);display:flex;align-items:center;justify-content:center}
.foot-bottom{position:absolute;top:254px;font-size:11.5px}
</style>
</head>
<body>

<header class="site-header">
  <span class="nav-link" style="left:164px">DESKS</span>
  <span class="nav-link" style="left:306px">FURNITURES</span>
  <span class="nav-link" style="left:434px">BEDS</span>
  <span class="brand">Brammvok</span>
  <span class="nav-link" style="left:746px">ABOUT</span>
  <span class="nav-link" style="left:879px">SERVICES</span>
  <span class="nav-link" style="left:1016px">CONTACT</span>
  <svg class="cart" width="26" height="26" viewBox="0 0 24 24" aria-label="Cart"><path d="M7 18a2 2 0 1 0 0 4 2 2 0 0 0 0-4zm10 0a2 2 0 1 0 0 4 2 2 0 0 0 0-4zM1 2h3.3l.9 2H22l-3.6 7.5c-.3.6-1 1-1.7 1H8.1l-1 1.8c-.1.2 0 .4.2.4H19v2H7c-1.5 0-2.4-1.6-1.7-2.9l1.4-2.5L3 4H1z" fill="#111"/></svg>
</header>

<section class="hero" role="img" aria-label="Black and white photo of a channel-tufted sofa between side tables and palms">
  <h1 class="hero-title center-x">NEW COLLECTION</h1>
  <div class="slide-arrow" style="left:83px;top:321px"><svg width="20" height="30" viewBox="0 0 20 30"><path d="M15 3 4 15l11 12" stroke="#444" stroke-width="2" fill="none"/></svg></div>
  <div class="slide-arrow" style="left:1070px;top:321px"><svg width="20" height="30" viewBox="0 0 20 30"><path d="M5 3l11 12L5 27" stroke="#444" stroke-width="2" fill="none"/></svg></div>
  <p class="hero-sub center-x">Hand-Crafted ,Custom-designed Furniture For Your Home, Office</p>
</section>

<h2 class="section-title center-x" style="top:872px">HAND-CRAFTED FURNITURE</h2>

<div class="tile" role="img" aria-label="Wooden sideboard with a plant under a chandelier" style="left:84px;top:947px;width:419px;height:379px;background:linear-gradient(180deg,#ecebe8 0%,#e6e4df 60%,#cdb59a 100%)"></div>
<div class="tile" role="img" aria-label="Green velvet sofa on a light wood floor" style="left:522px;top:947px;width:594px;height:379px;background:linear-gradient(180deg,#e4e3e1 0%,#dcdad7 50%,#2f5a4d 65%,#cdb79e 85%)"></div>
<span class="tile-label" style="left:298px;top:1347px">PRIMIUM PRODUCTS</span>
<span class="tile-label" style="left:823px;top:1347px">NEW COLLECTION</span>

<div class="tile" role="img" aria-label="Walnut office table with blue chairs" style="left:84px;top:1399px;width:594px;height:379px;background:linear-gradient(180deg,#e9e7e4 0%,#dcd6cf 40%,#6a4332 65%,#2b3a5a 85%,#e9e8e6 100%)"></div>
<div class="tile" role="img" aria-label="Beige armchair beside a white cabinet with a framed print" style="left:697px;top:1399px;width:419px;height:379px;background:linear-gradient(180deg,#d7c8b3 0%,#e3d7c6 45%,#c79f77 75%,#e8e2d8 100%)"></div>
<span class="tile-label" style="left:381px;top:1808px">OFFICE TABLE</span>
<span class="tile-label" style="left:911px;top:1808px">HOME FURNITURE</span>

<section class="feature" role="img" aria-label="Mid-century lounge chair with a potted plant on a wooden floor against a concrete wall">
  <div class="shop-btn">Shop Now</div>
</section>

<h2 class="section-title center-x" style="top:2682px;font-size:33px;letter-spacing:3px">EVERYDAY PURPOSE</h2>

<div class="tile" role="img" aria-label="Oak armchair with cream cushions" style="left:84px;top:2765px;width:332px;height:303px;background:linear-gradient(180deg,#e8e4dd 0%,#d9a05a 55%,#e3c49a 100%)"></div>
<div class="tile" role="img" aria-label="White shell chair next to a side table" style="left:434px;top:2765px;width:332px;height:303px;background:linear-gradient(180deg,#dfe4ea 0%,#eef0f2 55%,#d5d9dd 100%)"></div>
<div class="tile" role="img" aria-label="Green sofa with a wooden coffee table" style="left:784px;top:2765px;width:332px;height:303px;background:linear-gradient(180deg,#3c4a32 0%,#4f5d3a 40%,#8a5a36 70%,#3b2a20 100%)"></div>
<div class="carousel-arrow" style="left:84px"><svg width="14" height="22" viewBox="0 0 14 22"><path d="M11 2 3 11l8 9" stroke="#fff" stroke-width="2" fill="none"/></svg></div>
<div class="carousel-arrow" style="left:1072px"><svg width="14" height="22" viewBox="0 0 14 22"><path d="M3 2l8 9-8 9" stroke="#fff" stroke-width="2" fill="none"/></svg></div>

<span class="product-name" style="left:84px">Square Chair</span>
<span class="product-name" style="left:434px">Chair</span>
<span class="product-name" style="left:784px">Primium Chair</span>
<div class="price" style="left:84px;top:3118px"><i class="swatch" style="background:var(--tan)"></i>$500</div>
<div class="price" style="left:84px;top:3146px"><i class="swatch" style="background:var(--brown)"></i>$500</div>
<div class="price" style="left:434px;top:3118px"><i class="swatch" style="background:var(--tan)"></i>$500</div>
<div class="price" style="left:434px;top:3146px"><i class="swatch" style="background:var(--brown)"></i>$500</div>
<div class="price" style="left:784px;top:3118px"><i class="swatch" style="background:var(--tan)"></i>$500</div>
<div class="price" style="left:784px;top:3146px"><i class="swatch" style="background:var(--brown)"></i>$500</div>

<section class="connect">
  <div class="connect-photo" role="img" aria-label="Bright room with an arc floor lamp, round table, wooden chair and plants"></div>
  <span class="brand-small">Brammvok</span>
  <h3 class="connect-title">Lets Connect</h3>
  <span class="field-label" style="left:677px;top:3577px">FIRST NAME*</span>
  <span class="field-label" style="left:870px;top:3577px">LAST NAME*</span>
  <div class="field" style="left:678px;top:3604px;width:176px;height:48px"></div>
  <div class="field" style="left:870px;top:3604px;width:175px;height:48px"></div>
  <span class="field-label" style="left:677px;top:3666px">EMAIL ADDRESS*</span>
  <div class="field" style="left:678px;top:3695px;width:367px;height:50px"></div>
  <div class="submit-btn">Submit</div>
</section>

<h2 class="section-title center-x" style="top:4054px;font-size:40px;letter-spacing:1px">TESTIMINIALS</h2>
<div class="testimonial" style="left:246px">Lorem Ipsum is simply dummy text<br>of the typesetting industry.Lorem<br>Ipsum is simply dummy text<br>of the typesetting industry.<span class="testimonial-name">Elias Varnum</span></div>
<div class="testimonial" style="left:595px">Lorem Ipsum is simply dummy text<br>of the typesetting industry.Lorem<br>Ipsum is simply dummy text<br>of the typesetting industry.<span class="testimonial-name">Elias Varnum</span></div>
<div class="testimonial" style="left:945px">Lorem Ipsum is simply dummy text<br>of the typesetting industry.Lorem<br>Ipsum is simply dummy text<br>of the typesetting industry.<span class="testimonial-name">Elias Varnum</span></div>

<footer class="site-footer">
  <span class="foot-item" style="left:155px;top:48px">Our Story</span>
  <span class="foot-item" style="left:155px;top:85px">Careers</span>
  <span class="foot-item" style="left:155px;top:122px">Contact Us</span>
  <span class="foot-item" style="left:155px;top:159px">FAQs</span>
  <span class="foot-item" style="left:343px;top:48px">Furniture</span>
  <span class="foot-item" style="left:343px;top:85px">Hand-Crafted Furniture</span>
  <span class="foot-item" style="left:343px;top:122px">How to Buy &amp; Pay</span>
  <span class="foot-item" style="left:343px;top:159px">Inspiration</span>
  <span class="foot-item" style="left:576px;top:48px">Mailing- / Visiting address:</span>
  <span class="foot-item" style="left:576px;top:85px">Harlow Lane 24 12345 USA</span>
  <span class="foot-item" style="left:576px;top:122px">0198 765 432</span>
  <span class="foot-item" style="left:576px;top:159px">Gift Cards</span>
  <span class="foot-item" style="left:967px;top:48px">Follow Us</span>
  <span class="social-dot" style="left:967px"></span>
  <span class="social-dot" style="left:995px"></span>
  <span class="social-dot" style="left:1023px"></span>
  <div class="foot-email">Email</div>
  <div class="foot-signup">Sign Up</div>
  <span class="foot-bottom" style="left:155px;font-size:13px">© Company- All Rights Reserved</span>
  <span class="foot-bottom" style="left:748px">Terms and Conditions</span>
  <span class="foot-bottom" style="left:894px">Privacy Policy</span>
  <span class="foot-bottom" style="left:990px">Disclaimer</span>
</footer>

</body>
</html>
```